Promo Flyer to put in prize bags at carnival

I am owner of Copper & Lark Hair Salon located in Gahanna, OH. I’m sponsoring a community carnival when I will be putting flyers in all attendees prize bags. This flyer will communicate details of my salon on one side (picture of me, logo, description of business, address, website, email, phone #) and the other side will showcase and a 50% discount for first time customers. Flyer can be 5” x 7” or greater

Side 1 details:
-Logo will be attached to this brief
-picture of me will be attached to this brief
-address: 2561 W. Pellward Ave, Suite 17, Fenwick Hollow, ZZ, 00917
-website: clhairstudio.example
-email: Dorian.welby@clhairstudio.example
-phone: 614-52-BOOKS (26657)

Side 2 details:
-‘Guess what? You get 50% off your 1st service at Copper & Lark Hair Salon.’
-‘Expires 7/31/2018’
-Hair | Fashion | Photography
-Visit clhairstudio.example to book your service
-must present this flyer at time of service to receive discount

Hair And Beauty

Other font styles liked:
• Inoxida

Colors
3176b5
000000
ffffff

Must have
• 2 sides
• Color scheme to match logo

```html
<!DOCTYPE html>
<html lang="en">
<head>
<meta charset="utf-8">
<title>Copper &amp; Lark Hair Salon – Promo Flyer</title>
<link rel="stylesheet" href="https://fonts.googleapis.com/css2?family=Roboto:wght@400;500;700&family=Roboto+Condensed:wght@400;700&display=swap">
<style>
  :root {
    --backdrop: #dfe5e4;
    --space-deep: #131a4a;
    --space-mid: #242a6e;
    --space-violet: #3a2a6a;
    --space-green: #2c5a3a;
    --cyan: #6ff6fb;
    --brand-blue: #3f8fe8;
    --tag-blue: #4d8fe0;
    --white: #ffffff;
    --ink-blue: #3176b5;
  }
  * { box-sizing: border-box; margin: 0; padding: 0; }
  html, body {
    width: 1200px; height: 1200px; overflow: hidden;
    background: var(--backdrop);
    font-family: "Roboto", Arial, sans-serif;
  }
  .canvas { position: relative; width: 1200px; height: 1200px; }

  .flyer {
    position: absolute; top: 250px; width: 500px; height: 700px;
    overflow: hidden; color: var(--white);
    box-shadow: 0 18px 30px rgba(0,0,0,0.18);
  }
  .flyer--front { left: 60px; }
  .flyer--back { left: 640px; }

  .space-bg {
    position: absolute; inset: 0;
    background:
      radial-gradient(ellipse at 20% 70%, rgba(44,90,58,0.55), transparent 45%),
      radial-gradient(ellipse at 75% 30%, rgba(58,42,106,0.7), transparent 50%),
      linear-gradient(160deg, var(--space-mid), var(--space-deep));
  }

  /* Front side */
  .portrait {
    position: absolute; left: 150px; top: 60px; width: 300px; height: 640px;
    background: linear-gradient(180deg, #2a3050 0%, #1d3050 40%, #182440 100%);
    border-radius: 140px 140px 0 0;
    opacity: 0.9;
  }
  .brand { position: absolute; text-align: center; color: var(--white); }
  .brand__name { font-weight: 400; font-size: 30px; letter-spacing: 0.5px; white-space: nowrap; }
  .brand__name::before {
    content: ""; display: inline-block; width: 12px; height: 12px;
    border-radius: 50%; background: var(--brand-blue); margin-right: 10px; vertical-align: middle;
  }
  .brand__tagline {
    font-size: 11px; letter-spacing: 1px; margin-top: 4px;
    border-top: 1px solid rgba(255,255,255,0.6); padding-top: 4px;
  }
  .flyer--front .brand { right: 20px; top: 130px; }
  .flyer--front .brand__name { font-size: 24px; }

  .contact {
    position: absolute; left: 36px; bottom: 70px; list-style: none;
    font-family: "Roboto Condensed", Arial, sans-serif; font-size: 14px; line-height: 1.55;
  }
  .contact li { display: flex; align-items: flex-start; gap: 10px; }
  .contact svg { width: 13px; height: 13px; margin-top: 4px; flex: none; fill: var(--white); }

  /* Back side */
  .flyer--back .brand { left: 0; right: 0; top: 70px; }
  .flyer--back .brand__name { font-size: 40px; }
  .flyer--back .brand__tagline { width: 260px; margin: 6px auto 0; font-size: 12px; }
  .services {
    position: absolute; top: 160px; left: 0; right: 0; text-align: center;
    font-weight: 500; font-size: 30px;
  }
  .offer-band {
    position: absolute; top: 205px; left: 0; right: 0; height: 100px;
    background: var(--cyan); color: var(--brand-blue);
    display: flex; flex-direction: column; justify-content: center; align-items: center;
    font-weight: 500; font-size: 33px; line-height: 1.15;
  }
  .discount {
    position: absolute; top: 305px; left: 0; right: 0; height: 150px;
    display: flex; justify-content: center; align-items: center; gap: 14px;
  }
  .discount__number { font-weight: 500; font-size: 150px; line-height: 1; }
  .discount__tag {
    width: 82px; height: 120px; background: var(--tag-blue);
    clip-path: polygon(0 12%, 50% 0, 100% 12%, 100% 100%, 0 100%);
    display: flex; flex-direction: column; align-items: center; justify-content: center;
    padding-top: 10px;
  }
  .discount__tag b { font-size: 60px; font-weight: 700; line-height: 1; }
  .discount__tag span { font-size: 22px; font-weight: 500; }
  .cta {
    position: absolute; top: 458px; left: 0; right: 0; text-align: center;
    font-weight: 500; font-size: 44px;
  }
  .web-pill {
    position: absolute; top: 525px; left: 50%; transform: translateX(-50%);
    background: var(--tag-blue); border-radius: 24px; padding: 4px 26px;
    font-weight: 500; font-size: 30px; white-space: nowrap;
  }
  .expiry {
    position: absolute; top: 580px; left: 0; right: 0; text-align: center;
    font-weight: 500; font-size: 40px;
  }
  .terms {
    position: absolute; bottom: 0; left: 0; right: 0; height: 50px;
    background: var(--tag-blue); display: flex; align-items: center; justify-content: center;
    font-family: "Roboto Condensed", Arial, sans-serif; font-size: 19px;
  }
</style>
</head>
<body>
<main class="canvas">

  <section class="flyer flyer--front" aria-label="Flyer front: salon details">
    <div class="space-bg" role="img" aria-label="Deep blue and violet galaxy texture background"></div>
    <div class="portrait" role="img" aria-label="Photo of the salon owner in a navy suit and sunglasses"></div>
    <div class="brand">
      <p class="brand__name">Copper &amp; Lark</p>
      <p class="brand__tagline">An experience out of this world</p>
    </div>
    <ul class="contact">
      <li><svg viewBox="0 0 24 24"><path d="M6.6 10.8a15 15 0 0 0 6.6 6.6l2.2-2.2c.3-.3.7-.4 1-.2 1.1.4 2.3.6 3.6.6.6 0 1 .4 1 1V20c0 .6-.4 1-1 1A17 17 0 0 1 3 4c0-.6.4-1 1-1h3.5c.6 0 1 .4 1 1 0 1.3.2 2.5.6 3.6.1.3 0 .7-.2 1z"/></svg>614-52-BOOKS (26657)</li>
      <li><svg viewBox="0 0 24 24"><path d="M2 5h20v14H2z M2 5l10 8 10-8" fill="none" stroke="#fff" stroke-width="2"/></svg>Dorian.welby@clhairstudio.example</li>
      <li><svg viewBox="0 0 24 24"><circle cx="12" cy="12" r="9" fill="none" stroke="#fff" stroke-width="2"/><path d="M3 12h18M12 3c3 3 3 15 0 18M12 3c-3 3-3 15 0 18" fill="none" stroke="#fff" stroke-width="1.5"/></svg>clhairstudio.example</li>
      <li><svg viewBox="0 0 24 24"><path d="M12 2a7 7 0 0 0-7 7c0 5 7 13 7 13s7-8 7-13a7 7 0 0 0-7-7zm0 9.5A2.5 2.5 0 1 1 12 6.5a2.5 2.5 0 0 1 0 5z"/></svg>2561 W. Pellward Ave, Suite 17,<br>Fenwick Hollow, ZZ, 00917</li>
    </ul>
  </section>

  <section class="flyer flyer--back" aria-label="Flyer back: first-service discount">
    <div class="space-bg" role="img" aria-label="Deep blue and violet galaxy texture background"></div>
    <div class="brand">
      <p class="brand__name">Copper &amp; Lark</p>
      <p class="brand__tagline">An experience out of this world</p>
    </div>
    <p class="services">Hair • Fashion • Photography</p>
    <div class="offer-band">
      <span>Your 1st service at</span>
      <span>Copper &amp; Lark Hair Salon</span>
    </div>
    <div class="discount">
      <span class="discount__number">50</span>
      <span class="discount__tag"><b>%</b><span>OFF</span></span>
    </div>
    <p class="cta">Book Your Service</p>
    <p class="web-pill">clhairstudio.example</p>
    <p class="expiry">Expires 7/31/2018</p>
    <p class="terms">Must Present This Flyer at Time of Service to Receive Discount</p>
  </section>

</main>
</body>
</html>
```